Childcare Centre trifold brochure

Design a contemporary trifold brochure for a childcare centre that meets Australian printing requirements with supplied content, logo's, fonts and photo's. Please refer to the attached DL flyer front and back for similar possible style and content.

Target Market(s)

Families

Industry/Entity Type

Childcare

Requirements
Must have
• refer attached content, photo's, logo's and examples. Colours should be same as Pantone purple and green and or variations of. Refer attached dl flyer example.

```html
<!DOCTYPE html>
<html lang="en">
<head>
<meta charset="utf-8">
<title>Bright Sprouts – Trifold Brochure</title>
<link href="https://fonts.googleapis.com/css2?family=Open+Sans:ital,wght@0,400;0,600;0,700;0,800;1,600;1,700&display=swap" rel="stylesheet">
<style>
:root{
  --purple:#8a2f8e;
  --magenta:#b542a0;
  --green:#5cb82e;
  --lime:#c3dc1c;
  --orange:#f39a1e;
  --blue:#1f5fb8;
  --red:#d2323f;
  --ink:#2b2b2b;
  --grey:#555;
  --bg:#ececec;
}
*{box-sizing:border-box;margin:0;padding:0}
html,body{width:1200px;height:1200px;overflow:hidden;background:var(--bg)}
body{font-family:"Open Sans",sans-serif;color:var(--ink);position:relative}
.spread{position:absolute;left:230px;width:740px;height:570px;background:#fff;box-shadow:0 6px 18px rgba(0,0,0,.18);overflow:hidden}
.spread--outside{top:20px}
.spread--inside{top:610px}
.panel{position:absolute;top:0;width:246.67px;height:570px;overflow:hidden}
.p1{left:0}.p2{left:246.67px}.p3{left:493.33px}
.abs{position:absolute}
.purple-block{background:linear-gradient(90deg,var(--purple),var(--magenta));color:#fff}
.photo{position:absolute}
/* outside panel 1 */
.intro-quote{left:0;top:0;width:100%;height:125px;padding:30px 22px 0 22px;font-size:9.4px;font-weight:700;line-height:1.3;text-align:justify}
.intro-photo{left:0;top:125px;width:100%;height:290px;background:linear-gradient(160deg,#c9b79a,#7a6a4f 45%,#6a4aa0 70%,#8a6c4c)}
.belief{left:0;top:415px;width:100%;height:155px;padding:17px 22px;font-size:9.6px;line-height:1.27;text-align:justify}
/* outside panel 2 */
.garden-photo{left:0;top:0;width:100%;height:166px;background:linear-gradient(180deg,#6f9d4a,#b3b0a6 45%,#8f7a60)}
.green-rule{left:0;top:166px;width:100%;height:3px;background:var(--green)}
.louv{left:22px;top:184px;width:204px;font-size:10px;font-weight:700;font-style:italic;text-align:center;line-height:1.28}
.louv-cite{right:22px;top:302px;font-size:10.6px;font-weight:600}
.brand{display:flex;align-items:center;gap:4px;color:var(--green);font-weight:800}
.brand .dot{width:12px;height:12px;border-radius:50%;background:var(--purple);flex:none}
.brand-small{left:0;width:100%;top:340px;justify-content:center;font-size:12px}
.partners{left:24px;top:382px;display:flex;gap:18px;align-items:center}
.partners span{display:block;background:#e8e8e8;border-radius:3px}
.contact{left:0;top:415px;width:100%;height:99px;padding:12px 18px 0 24px;font-size:9.6px}
.contact-row{display:flex;gap:12px;align-items:flex-start;padding:5px 0;border-bottom:1px dashed rgba(255,255,255,.6)}
.contact-row:last-child{border-bottom:none}
.contact-row svg{flex:none;margin-top:1px}
.contact-row.web{font-weight:700;font-style:italic}
.hours{left:20px;top:524px;font-size:9.8px;line-height:1.2}
.hours .label{color:var(--purple);font-size:7px;font-weight:700;font-style:italic}
.hours .note{color:var(--purple);font-size:6.6px;font-style:italic}
.social{left:150px;top:528px;text-align:center}
.social .icons{display:flex;gap:9px;justify-content:center;margin-bottom:6px}
.social .icons i{display:block;width:13px;height:13px;border-radius:50%}
.social .handle{color:var(--purple);font-size:8.4px;font-weight:700;font-style:italic}
/* outside panel 3 */
.cover-photo{left:0;top:0;width:100%;height:480px;background:linear-gradient(180deg,#e6e2cf 0,#5d9a3e 20%,#7e8b8e 45%,#a38466 75%)}
.swoosh{left:0;top:0}
.award{position:absolute;border-radius:50%}
.award--a{background:var(--red);width:62px;height:62px;left:43px;top:19px}
.award--b{background:var(--magenta);width:86px;height:86px;left:54px;top:167px}
.award--c{background:var(--orange);width:70px;height:70px;left:161px;top:172px}
.award--d{background:var(--blue);width:98px;height:98px;left:28px;top:276px}
.cover-brand{left:0;width:100%;top:448px;flex-direction:column;gap:5px}
.cover-brand .dot{width:30px;height:30px}
.cover-brand .name{font-size:19px}
.cover-brand .sub{font-size:7.4px;color:var(--green);font-weight:600}
.cover-foot{left:18px;right:16px;top:530px;display:flex;justify-content:space-between;align-items:flex-end;color:var(--purple)}
.cover-foot .mail{font-size:6.4px;font-style:italic}
.cover-foot .phone{font-size:14px;text-align:right;line-height:1.1}
.cover-foot .phone small{display:block;font-size:9px;font-weight:700;font-style:italic}
/* inside */
.strip{position:absolute;top:0;height:105px}
.strip-a{left:0;width:246.67px;background:linear-gradient(120deg,#b07ad0,#6a4a3a 50%,#c04a3a)}
.strip-b{left:246.67px;width:246.67px;background:linear-gradient(120deg,#c8521e,#8a5a3a 45%,#d2a070)}
.body-col{position:absolute;top:133px;left:22px;width:203px;font-size:7.7px;line-height:1.27;color:var(--grey);text-align:justify}
.body-col p{margin-bottom:8px}
.p2 .body-col{top:134px;left:22px}
.facts{left:0;top:0;width:100%;height:192px;padding:30px 22px 0 22px;font-size:7.5px;font-weight:700;line-height:1.3;text-align:justify}
.facts p{margin-bottom:8px}
.p3 .body-col{top:213px;font-size:8.2px}
.thumb{position:absolute;top:441px;height:113px;background:linear-gradient(160deg,#8a6a4a,#6a3f9e 45%,#a08a70)}
.p2 .t1{left:0;width:105px}
.p2 .t2{left:133px;width:110px}
.p3 .t3{left:22px;width:85px}
.inner-brand{left:125px;top:470px;flex-direction:column;gap:3px;width:120px}
.inner-brand .dot{width:22px;height:22px}
.inner-brand .name{font-size:12.5px}
.inner-brand .sub{font-size:5.2px;font-weight:600}
.inner-brand .url{margin-top:14px;color:var(--purple);font-size:8.4px;font-weight:700;font-style:italic}
.rainbow{position:absolute;left:0;bottom:0;width:100%;height:16px;background:linear-gradient(90deg,var(--green),var(--lime) 40%,#f2c21b 55%,var(--orange) 65%,var(--magenta) 85%,var(--purple))}
</style>
</head>
<body>

<section class="spread spread--outside">
  <div class="panel p1">
    <p class="abs purple-block intro-quote">“Early childhood is the most important time for brain development. It is the time in a child's life where they start building their brain connections and therefore, ultimately, the work we do will shape their life forever”.</p>
    <div class="photo intro-photo" role="img" aria-label="Children in purple hats and rain suits walking along a log path in the garden"></div>
    <p class="abs purple-block belief">We believe that the best developmental outcomes occur when children who wander, wonder and play are also learning. It happens when children's interests and passions are respected and nurtured and when educators shift their agenda away from imparting knowledge that we consider worthy, to showing children that we value their curiosity, problem solving, questions, and theories.</p>
  </div>

  <div class="panel p2">
    <div class="photo garden-photo" role="img" aria-label="Nature playground with tree, log seating and mulch"></div>
    <div class="abs green-rule"></div>
    <p class="abs louv">“Passion is lifted from the earth itself by the muddy hands of the young; it travels along grass stained sleeves to the heart. If we are going to save environmentalism and the environment, we must also save an endangered indicator species: the child in nature.”</p>
    <p class="abs louv-cite">Jordan Ashby</p>
    <div class="abs brand brand-small"><span class="dot"></span>Bright Sprouts</div>
    <div class="abs partners">
      <span style="width:62px;height:26px"></span>
      <span style="width:82px;height:26px"></span>
      <span style="width:20px;height:26px"></span>
    </div>
    <div class="abs purple-block contact">
      <div class="contact-row">
        <svg width="10" height="12" viewBox="0 0 10 12"><path d="M5 0a4 4 0 0 1 4 4c0 3-4 8-4 8S1 7 1 4a4 4 0 0 1 4-4z" fill="#fff"/><circle cx="5" cy="4" r="1.6" fill="#9a3696"/></svg>
        <span>18 Wattle Lane, Banksia Grove,<br>WA 6031</span>
      </div>
      <div class="contact-row">
        <svg width="11" height="8" viewBox="0 0 11 8"><rect width="11" height="8" fill="#fff"/><path d="M0 0l5.5 4.5L11 0" stroke="#9a3696" fill="none"/></svg>
        <span>hello@brightsprouts.com.au</span>
      </div>
      <div class="contact-row web">
        <svg width="10" height="10" viewBox="0 0 10 10"><circle cx="5" cy="5" r="4.4" fill="none" stroke="#fff"/><path d="M.6 5h8.8M5 .6c2.4 2.6 2.4 6.2 0 8.8M5 .6c-2.4 2.6-2.4 6.2 0 8.8" stroke="#fff" fill="none" stroke-width=".8"/></svg>
        <span>www.brightsprouts.com.au</span>
      </div>
    </div>
    <div class="abs hours">
      <div class="label">Opening Hours:</div>
      6:00am to 6:00pm<br>Monday to Friday
      <div class="note">(except public holidays)</div>
    </div>
    <div class="abs social">
      <div class="icons"><i style="background:var(--blue)"></i><i style="background:var(--magenta)"></i><i style="background:#3aa0e8"></i></div>
      <div class="handle">brightsproutsAU</div>
    </div>
  </div>

  <div class="panel p3">
    <div class="photo cover-photo" role="img" aria-label="Outdoor play area with shade sail, cubby house and sandpit"></div>
    <svg class="abs swoosh" width="247" height="570" viewBox="0 0 247 570" aria-hidden="true">
      <defs><linearGradient id="sw" x1="0" x2="1" y1="1" y2="0"><stop offset="0" stop-color="#3aa535"/><stop offset="1" stop-color="#d4e21c"/></linearGradient></defs>
      <path d="M0 440C100 430 200 330 247 160L247 230C200 370 100 460 0 478Z" fill="url(#sw)"/>
      <path d="M0 478C100 460 200 370 247 230L247 570L0 570Z" fill="#fff"/>
    </svg>
    <div class="award award--a" role="img" aria-label="Quality rating award seal"></div>
    <div class="award award--b" role="img" aria-label="Service of the year finalist award seal"></div>
    <div class="award award--c" role="img" aria-label="Director of the year finalist award seal"></div>
    <div class="award award--d" role="img" aria-label="State director of the year winner award seal"></div>
    <div class="abs brand cover-brand"><span class="dot"></span><span class="name">Bright Sprouts</span><span class="sub">Early Learning Centre</span></div>
    <div class="abs cover-foot">
      <span class="mail">hello@brightsprouts.com.au</span>
      <span class="phone">08 9400 1234<small>brightsprouts.com.au</small></span>
    </div>
  </div>
</section>

<section class="spread spread--inside">
  <div class="strip strip-a" role="img" aria-label="Children in purple hats preparing vegetables at an outdoor table"></div>
  <div class="strip strip-b" role="img" aria-label="Timber water play trough in the nature playground"></div>

  <div class="panel p1">
    <div class="body-col">
      <p>We are a Reggio Emilia inspired Childcare Centre offering long day care and a Nature Kindergarten program for 3 – 6-year olds.</p>
      <p>At the core of our program is a Child-First ‘emergent curriculum’. An emergent Curriculum can be defined as a way of supporting learning that is based on the children's interests.</p>
      <p>Learning occurs naturally, children thrive and learn best when their interests are considered and captured.</p>
      <p>Which means our Educators act as mentors for the children as they guide them through the adventure of learning outdoors in academic subjects such as science, technology, engineering and maths (STEM).</p>
      <p>Our children spend their days predominantly outdoors all year round in one of two amazing large Naturescape playgrounds full of native trees, a running creek bed, large stepping logs, a herb, vegetable and bush tucker garden along with a recycled mud kitchen made by the children, worm farm, compost bin and chickens and a fire pit where the older children can cook over an open fire.</p>
      <p>The children are taught real life skills and do their own individual risk assessments before engaging in learning experience such as crossing a flowing river creek bed, walking along logs, and climbing &amp; jumping off trees. They also learn whittling, lighting fires (using steel flints), use proper hand tools such as hacksaws, hammers and manual hand drills and learn how to navigate uneven terrains.</p>
      <p>The significant importance of learning through play while outdoors in a natural environment cannot be underestimated.</p>
      <p>Just as importantly the children are able to explore and</p>
    </div>
  </div>

  <div class="panel p2">
    <div class="body-col">
      <p>play at their own pace and set their own rhythm.</p>
      <p>In relation to children's wellbeing, long-term outdoor preschool programmes were found to have positive impacts on both children's physical and mental health. The studies found that as well as promoting wellbeing in children, the programmes enhance their confidence and resilience, persistence and problem-solving skills.</p>
      <p>Children's confidence increased, and they had heightened levels of self-belief, positive attitude, independence and demonstrated an increased ability to take initiatives.</p>
      <p>Children who play regularly in natural settings are sick less often. Mud, sand, water, leaves, sticks, pine cones and gum nuts can help to stimulate children's immune system as well as their imagination.</p>
      <p>Children who spend more time outside tend to be more physically active and are less likely to be overweight. They are more resistant to stress; have lower incidence of behavioural disorders, anxiety and depression; and have a higher measure of self-worth.</p>
      <p>Children who play in natural settings play in more diverse, imaginative and creative ways and show improved language and collaboration skills They also have more positive feelings about each other.</p>
    </div>
    <div class="thumb t1" role="img" aria-label="Toddler in purple hat using a hand drill on a log"></div>
    <div class="thumb t2" role="img" aria-label="Child in purple hat crouching to work with tools on the ground"></div>
  </div>

  <div class="panel p3">
    <div class="abs purple-block facts">
      <p>“providing outdoor opportunities for learning is a critical priority for parents, teachers and the wider community”</p>
      <p>“outdoor learning was added to the Australian Curriculum in 2015, however just 34% of teachers surveyed taught outdoors for 15 minutes or more”</p>
      <p>“Nature ignites passion, inspiration, creativity &amp; purpose and plays an important role in the cognitive, emotional and physical development of children”</p>
      <p>Source: Growing Outdoors: Lessons for Future Generations' report, Published July 2017</p>
    </div>
    <div class="body-col">
      <p>Since 2015, throughout each school term our educators run free lessons for all ages in the following: yoga, meditation, sign language, Spanish, German, Malaysian, Sri Lankan Culture, Sustainability, Noongar Culture &amp; Sport.</p>
      <p>The sign language is a particular hit with the mothers as the babies are able to sign to their parents when they are hungry or need to go to the toilet before they even start talking.</p>
      <p>The first five years of a child's development are the most crucial with 90% of their brain synapsis being formed by this time.</p>
      <p>Becoming multilingual or being able to sign has an expediential effect on the children's development outcomes which is why we offer such a vast array of authentic leaning experiences.</p>
    </div>
    <div class="thumb t3" role="img" aria-label="Small child in purple hat sitting on the ground outdoors"></div>
    <div class="abs brand inner-brand"><span class="dot"></span><span class="name">Bright Sprouts</span><span class="sub">Early Learning Centre</span><span class="url">brightsprouts.com.au</span></div>
  </div>

  <div class="rainbow"></div>
</section>

</body>
</html>
```